Letterhead Design for Law Firm that Specializes in Property Damage Litigation

We are looking for a redesign of our letterhead. Our current letterhead lists all of our current staff members and we'd like to come up with a design that does NOT list all of the staff members so that it does not need to be updated with every newly hired employee. Must be in editable format.

We are a law firm that specializes in property damage, so we need something that is professional, yet modern. The final design should use our existing logo and should use a blue color scheme (alternate colors would be gray, black, and white).

Industry/Entity Type

Legal

Colors
0054AA
0677BA
7BADD7
CADEEF
E8F1F8

```html
<!DOCTYPE html>
<html lang="en">
<head>
<meta charset="UTF-8">
<title>Hartwell Corso &amp; Linden — Letterhead</title>
<link href="https://fonts.googleapis.com/css2?family=Tinos:wght@400;700&display=swap" rel="stylesheet">
<style>
  :root {
    --navy: #1c3a6e;
    --ink: #4a4a4a;
    --muted: #707070;
    --paper: #ffffff;
    --backdrop: #ececec;
  }
  * { box-sizing: border-box; margin: 0; padding: 0; }
  html, body {
    width: 1200px;
    height: 900px;
    overflow: hidden;
    background: var(--backdrop);
    font-family: "Tinos", "Times New Roman", serif;
  }
  .canvas {
    position: relative;
    width: 1200px;
    height: 900px;
  }
  .letterhead {
    position: absolute;
    left: 275px;
    top: 25px;
    width: 650px;
    height: 850px;
    background: var(--paper);
    border: 7px solid var(--navy);
    box-shadow: 0 3px 10px rgba(0,0,0,0.12);
  }
  .masthead {
    position: absolute;
    top: 42px;
    left: 0;
    right: 0;
    text-align: center;
  }
  .firm-brand {
    display: inline-flex;
    align-items: center;
    gap: 10px;
  }
  .brand-mark {
    width: 16px;
    height: 16px;
    background: var(--navy);
  }
  .firm-name {
    color: var(--navy);
    font-weight: 700;
    font-size: 20px;
    letter-spacing: 1px;
    text-transform: uppercase;
  }
  .tagline {
    margin-top: 8px;
    color: var(--muted);
    font-size: 8.5px;
    letter-spacing: 2.6px;
    text-transform: uppercase;
  }
  .website {
    margin-top: 4px;
    color: var(--navy);
    font-weight: 700;
    font-size: 11px;
    letter-spacing: 3px;
  }
  .office-footer {
    position: absolute;
    bottom: 40px;
    left: 0;
    right: 0;
    text-align: center;
    color: var(--ink);
    font-size: 12px;
    line-height: 1.5;
  }
  .office + .office { margin-top: 10px; }
  .office-title {
    color: var(--navy);
    font-weight: 700;
    font-size: 13px;
    letter-spacing: 0.3px;
    text-transform: uppercase;
    margin-bottom: 4px;
  }
  .office-line {
    display: flex;
    justify-content: center;
    align-items: center;
    gap: 4px;
  }
  .icon {
    width: 11px;
    height: 11px;
    fill: var(--navy);
    flex: none;
  }
  .divider { color: var(--muted); margin: 0 3px; }
</style>
</head>
<body>
<div class="canvas">
  <section class="letterhead">
    <header class="masthead">
      <div class="firm-brand">
        <span class="brand-mark"></span>
        <span class="firm-name">Hartwell Corso &amp; Linden</span>
      </div>
      <p class="tagline">The Property Damage Attorneys</p>
      <p class="website">www.hclegal.com</p>
    </header>

    <footer class="office-footer">
      <div class="office">
        <p class="office-title">Philadelphia Office</p>
        <p class="office-line">
          <svg class="icon" viewBox="0 0 12 12"><path d="M1 4c0-1.5 2-3 5-3s5 1.5 5 3v1H8.5V3.8h-5V5H1z M2.5 6h7l1 5h-9z"/></svg>
          (215) 555-0140
          <span class="divider">|</span>
          <svg class="icon" viewBox="0 0 12 12"><path d="M3 1h6v3H3z M1 5h10v5H9V8H3v2H1z M3.5 8.5h5V11h-5z"/></svg>
          (215) 555-0188
        </p>
        <p class="office-line">
          <svg class="icon" viewBox="0 0 12 12"><path d="M6 0.5a4 4 0 0 1 4 4c0 3-4 7-4 7s-4-4-4-7a4 4 0 0 1 4-4zm0 2.3a1.7 1.7 0 1 0 0 3.4 1.7 1.7 0 0 0 0-3.4z"/></svg>
          820 Market Square Blvd. Suite 410, Philadelphia, PA 19107
        </p>
      </div>
      <div class="office">
        <p class="office-title">New Jersey Office</p>
        <p class="office-line">
          <svg class="icon" viewBox="0 0 12 12"><path d="M1 4c0-1.5 2-3 5-3s5 1.5 5 3v1H8.5V3.8h-5V5H1z M2.5 6h7l1 5h-9z"/></svg>
          (856) 555-0162
          <span class="divider">|</span>
          <svg class="icon" viewBox="0 0 12 12"><path d="M3 1h6v3H3z M1 5h10v5H9V8H3v2H1z M3.5 8.5h5V11h-5z"/></svg>
          (856) 555-0197
        </p>
        <p class="office-line">
          <svg class="icon" viewBox="0 0 12 12"><path d="M6 0.5a4 4 0 0 1 4 4c0 3-4 7-4 7s-4-4-4-7a4 4 0 0 1 4-4zm0 2.3a1.7 1.7 0 1 0 0 3.4 1.7 1.7 0 0 0 0-3.4z"/></svg>
          275 Haddon Park Road, Suite 120, Cherry Hill, NJ 08002
        </p>
      </div>
    </footer>
  </section>
</div>
</body>
</html>
```